Business Card Design

No logos or construction designs

Easy to read Ray Tolliver Roofing, LLC (in red)

all other lettering in black I guess I am open to what the designers come up

Industry/Entity Type

Construction

Contact Information for Business Card

Ray Tolliver Roofing, LLC office 555-2189063 fax 555-318-940 3075 Marrowfield W Massillon, Ohio 40000
Ray@RayTolliverRoofing.example Residential Commerical
Ray Tolliver cell 555-862-1375

```html
<!DOCTYPE html>
<html lang="en">
<head>
<meta charset="utf-8">
<title>Ray Tolliver Roofing, LLC — Business Card</title>
<link rel="stylesheet" href="https://fonts.googleapis.com/css2?family=Cinzel:wght@700&family=Encode+Sans+Condensed:wght@300;400&display=swap">
<style>
  :root {
    --brand-red: #e81f4a;
    --text-grey: #666669;
    --paper: #ffffff;
  }
  html, body {
    margin: 0;
    padding: 0;
    overflow: hidden;
    background: var(--paper);
  }
  .card {
    position: relative;
    width: 1200px;
    height: 703px;
    background: var(--paper);
    overflow: hidden;
    font-family: "Encode Sans Condensed", "Arial Narrow", sans-serif;
    color: var(--text-grey);
  }
  .company-name {
    position: absolute;
    right: 172px;
    top: 270px;
    margin: 0;
    font-family: "Cinzel", "Copperplate", serif;
    font-weight: 700;
    font-size: 52px;
    line-height: 1;
    letter-spacing: 1.5px;
    color: var(--brand-red);
    white-space: nowrap;
  }
  .services {
    position: absolute;
    right: 176px;
    top: 328px;
    margin: 0;
    font-size: 39px;
    font-weight: 400;
    line-height: 1.1;
    white-space: nowrap;
  }
  .address {
    position: absolute;
    right: 622px;
    top: 510px;
    margin: 0;
    font-style: normal;
    font-weight: 300;
    font-size: 30px;
    line-height: 42px;
    text-align: right;
    white-space: nowrap;
  }
  .divider {
    position: absolute;
    left: 604px;
    top: 476px;
    width: 5px;
    height: 157px;
    background: var(--brand-red);
  }
  .contact-list {
    position: absolute;
    left: 635px;
    top: 472px;
    margin: 0;
    padding: 0;
    list-style: none;
    font-weight: 300;
    font-size: 30px;
    line-height: 41px;
    white-space: nowrap;
  }
</style>
</head>
<body>
  <main class="card">
    <h1 class="company-name">Ray Tolliver Roofing, LLC</h1>
    <p class="services">Residential Commerical</p>

    <address class="address">
      3075 Marrowfield W<br>
      Massillon, Ohio 40000
    </address>

    <div class="divider" aria-hidden="true"></div>

    <ul class="contact-list">
      <li class="contact-office">Office 555.218.9063</li>
      <li class="contact-cell">Cell 555.862.1375</li>
      <li class="contact-fax">Fax 555.318.940</li>
      <li class="contact-email">Ray@RayTolliverRoofing.example</li>
    </ul>
  </main>
</body>
</html>
```